Outpost Lattice Advisors – Franchise Growth & Development Presentation

Outpost Lattice Advisors is an outsourced franchise sales organization (FSO) that helps franchisors grow their franchise systems without the expense and risk of hiring an internal franchise development team.

We are seeking a professional PowerPoint presentation that will be used to present our services to franchisors, franchise executives, founders, and growth-stage franchise brands.

The presentation should communicate the value of partnering with Outpost Lattice Advisors, including:

• Fractional franchise sales team versus hiring internal staff
• 30+ years of franchise industry experience
• 550+ franchise sales successes
• Immediate access to established franchise broker relationships
• Proven franchise development processes
• Franchise growth strategy and enterprise value creation
• Potential private equity and exit opportunities through franchise expansion

The presentation should feel like a modern consulting, investment, or growth strategy presentation rather than a typical sales brochure. We want strong visual storytelling, custom infographics, professional diagrams, and clean business-oriented design.

The audience includes business owners, franchise founders, franchise executives, and investors who are evaluating growth strategies for their franchise systems.

Target Market(s)

Primary Audience: Emerging franchisors Growth-stage franchise brands Franchise founders Franchise CEOs Franchise presidents Franchise development executives Secondary Audience: Private equity firms Franchise investors Strategic buyers Franchise consultants

Industry/Entity Type

Franchise Development, Private Equity / Business Expansion

Font styles to use
Other font styles liked:
• Use Montserrat for titles and Open Sans for body text.

Requirements
Must have
• Modern professional business design Consistent branding throughout Custom infographics Comparison graphics Broker network ecosystem graphic Enterprise value graphic Easy-to-read charts and visuals Editable PowerPoint format Professional iconography. www.outpostlatticeadvisors.example as reference for colors
Nice to have
• Franchise-related imagery Subtle growth-themed visuals Timeline graphics Data visualization Private equity / valuation style graphics
Should not have
• Cartoon graphics Clip art Overly busy slides Stock-template appearance Bright neon colors Handwritten fonts Excessive text on slides Juvenile or playful design elements

```html
<!DOCTYPE html>
<html lang="en">
<head>
<meta charset="UTF-8">
<title>Services We Provide – Outpost Lattice Advisors</title>
<link rel="stylesheet" href="https://fonts.googleapis.com/css2?family=Poppins:wght@600;700&display=swap">
<style>
  :root {
    --navy: #11304f;
    --orange: #f39200;
    --page: #f7f8fa;
    --card: #ffffff;
    --ring: #ffffff;
  }
  * { margin: 0; padding: 0; box-sizing: border-box; }
  html, body { width: 1200px; height: 675px; overflow: hidden; background: var(--page); }
  .slide {
    position: relative;
    width: 1200px;
    height: 675px;
    background: var(--page);
    font-family: "Poppins", Arial, sans-serif;
    color: var(--navy);
  }
  .top-rule {
    position: absolute;
    left: 77px; top: 57px;
    width: 892px; height: 1.5px;
    background: var(--orange);
  }
  .brand {
    position: absolute;
    left: 980px; top: 47px;
    width: 146px;
    text-align: right;
    font-size: 11px;
    font-weight: 700;
    letter-spacing: 0.2px;
    color: var(--navy);
    white-space: nowrap;
  }
  .title {
    position: absolute;
    left: 74px; top: 94px;
    font-size: 50px;
    font-weight: 700;
    letter-spacing: -0.5px;
    line-height: 1.2;
  }
  .title-bar {
    position: absolute;
    left: 77px; top: 165px;
    width: 90px; height: 7px;
    border-radius: 4px;
    background: var(--orange);
  }
  .services {
    position: absolute;
    left: 84px; top: 233px;
    display: grid;
    grid-template-columns: repeat(4, 240px);
    grid-template-rows: repeat(2, 142px);
    column-gap: 26px;
    row-gap: 56px;
  }
  .service-card {
    position: relative;
    background: var(--card);
    border-radius: 10px;
    box-shadow: 2px 3px 6px rgba(17, 48, 79, 0.16);
  }
  .service-badge {
    position: absolute;
    left: 70px; top: -36px;
    width: 100px; height: 100px;
    overflow: visible;
  }
  .service-label {
    position: absolute;
    left: 0; right: 0; top: 76px;
    text-align: center;
    font-size: 17.5px;
    font-weight: 600;
    line-height: 1.22;
    letter-spacing: -0.3px;
  }
  .footer-label {
    position: absolute;
    left: 78px; top: 617px;
    font-size: 12.5px;
    font-weight: 700;
    letter-spacing: 1.9px;
    color: var(--navy);
  }
  .footer-rule {
    position: absolute;
    left: 356px; top: 626px;
    width: 767px; height: 1.5px;
    background: var(--orange);
  }
  .icon { fill: none; stroke: #fff; stroke-width: 1.4; stroke-linecap: round; stroke-linejoin: round; }
</style>
</head>
<body>
<div class="slide">
  <div class="top-rule"></div>
  <div class="brand">OUTPOST LATTICE ADVISORS</div>

  <h1 class="title">Services We Provide</h1>
  <div class="title-bar"></div>

  <svg width="0" height="0" style="position:absolute">
    <defs>
      <filter id="ring-shadow" x="-20%" y="-20%" width="140%" height="140%">
        <feDropShadow dx="0" dy="1" stdDeviation="1.2" flood-color="#11304f" flood-opacity="0.12"/>
      </filter>
      <g id="badge-base">
        <circle cx="50" cy="50" r="45" fill="var(--ring)" filter="url(#ring-shadow)"/>
        <path d="M8.3 33.1 A45 45 0 1 0 91.7 33.1" fill="none" stroke="var(--orange)" stroke-width="1.2"/>
        <circle cx="8.3" cy="33.1" r="1.3" fill="var(--orange)"/>
        <circle cx="91.7" cy="33.1" r="1.3" fill="var(--orange)"/>
        <circle cx="50" cy="95" r="3" fill="var(--orange)"/>
        <circle cx="50" cy="50" r="36" fill="var(--navy)"/>
      </g>
    </defs>
  </svg>

  <div class="services">
    <div class="service-card">
      <svg class="service-badge" viewBox="0 0 100 100" aria-hidden="true">
        <use href="#badge-base"/>
        <g class="icon" transform="translate(32 32) scale(1.5)">
          <circle cx="16" cy="7" r="4.5"/>
          <circle cx="16" cy="6" r="1.4"/>
          <path d="M13.4 10.2c.6-1.6 4.6-1.6 5.2 0"/>
          <path d="M9 10 4.5 14.5a3.5 3.5 0 0 0 5 5L14 15"/>
          <path d="M7 12.5l2 2M11.5 17l2-2"/>
          <path d="M11 9l1-1M13 12l1.5-1"/>
        </g>
      </svg>
      <div class="service-label">FDD / Operations<br>Review</div>
    </div>

    <div class="service-card">
      <svg class="service-badge" viewBox="0 0 100 100" aria-hidden="true">
        <use href="#badge-base"/>
        <g class="icon" transform="translate(32 32) scale(1.5)">
          <circle cx="12" cy="8" r="3"/>
          <circle cx="6.5" cy="9" r="2.4"/>
          <circle cx="17.5" cy="9" r="2.4"/>
          <path d="M6.5 18c0-3.5 2.5-6 5.5-6s5.5 2.5 5.5 6z"/>
          <path d="M2.5 18c0-2.7 1.6-4.6 4-4.6M21.5 18c0-2.7-1.6-4.6-4-4.6"/>
        </g>
      </svg>
      <div class="service-label">Franchise Sales<br>Outsourcing</div>
    </div>

    <div class="service-card">
      <svg class="service-badge" viewBox="0 0 100 100" aria-hidden="true">
        <use href="#badge-base"/>
        <g class="icon" transform="translate(32 32) scale(1.5)" stroke-width="1.8">
          <path d="M4.5 5.5h15l-5.5 7v6l-4 2v-8z"/>
        </g>
      </svg>
      <div class="service-label">Lead<br>Qualification</div>
    </div>

    <div class="service-card">
      <svg class="service-badge" viewBox="0 0 100 100" aria-hidden="true">
        <use href="#badge-base"/>
        <g class="icon" transform="translate(32 32) scale(1.5)">
          <path d="M10 20v-3.5C7.5 15 7 13 7 11a5.5 5.5 0 0 1 11 0l1.5 3h-1.5v2.5h-2.5v3.5"/>
          <path d="M12.5 5.5V2.5"/>
          <path d="M12.5 3.5c-1-1.8-2.8-1.8-3.5-1 .7 1.2 2 1.6 3.5 1z"/>
          <path d="M12.5 3.5c1-1.8 2.8-1.8 3.5-1-.7 1.2-2 1.6-3.5 1z"/>
        </g>
      </svg>
      <div class="service-label">Candidate<br>Nurturing</div>
    </div>

    <div class="service-card">
      <svg class="service-badge" viewBox="0 0 100 100" aria-hidden="true">
        <use href="#badge-base"/>
        <g class="icon" transform="translate(32 32) scale(1.5)">
          <rect x="3.5" y="5" width="17" height="15" rx="1.5"/>
          <path d="M3.5 9h17M8 3v4M16 3v4"/>
          <path d="M12 10.8l1.1 2.3 2.5.3-1.8 1.7.5 2.5-2.3-1.3-2.3 1.3.5-2.5-1.8-1.7 2.5-.3z"/>
        </g>
      </svg>
      <div class="service-label">Discovery Day<br>Coordination</div>
    </div>

    <div class="service-card">
      <svg class="service-badge" viewBox="0 0 100 100" aria-hidden="true">
        <use href="#badge-base"/>
        <g class="icon" transform="translate(32 32) scale(1.5)">
          <path d="M1.5 9l2-3.5 3 1.5-2 4z"/>
          <path d="M22.5 9l-2-3.5-3 1.5 2 4z"/>
          <path d="M6 8l3-1.5h3l-3 2.5c.8 1 2 1 3 .2l2-1.2 4.5 4"/>
          <path d="M5 11l5 5.5c.6.6 1.4.4 1.8-.2M8 13l3.5 3.3M9.5 11.5l3.5 3.3c.6.5 1.4.2 1.6-.4M12 10.5l3 2.8c.6.5 1.4.2 1.5-.5"/>
          <path d="M18 11.8l-2.5-2"/>
        </g>
      </svg>
      <div class="service-label">Broker Recruitment<br>/ Engagement</div>
    </div>

    <div class="service-card">
      <svg class="service-badge" viewBox="0 0 100 100" aria-hidden="true">
        <use href="#badge-base"/>
        <g class="icon" transform="translate(32 32) scale(1.5)">
          <rect x="4.5" y="5" width="15" height="11" rx="1"/>
          <path d="M2.5 18.5h19l-1 1.5h-17z"/>
          <path d="M10 8.8 8 10.5l2 1.7M14 8.8l2 1.7-2 1.7"/>
        </g>
      </svg>
      <div class="service-label">CRM<br>Management</div>
    </div>

    <div class="service-card">
      <svg class="service-badge" viewBox="0 0 100 100" aria-hidden="true">
        <use href="#badge-base"/>
        <g class="icon" transform="translate(32 32) scale(1.5)">
          <path d="M3 20.5h18"/>
          <rect x="4.5" y="16" width="2.5" height="4.5"/>
          <rect x="9" y="13" width="2.5" height="7.5"/>
          <rect x="13.5" y="11" width="2.5" height="9.5"/>
          <rect x="18" y="8" width="2.5" height="12.5"/>
          <path d="M3.5 13 8.5 8.5l3 2.5 8-7"/>
          <path d="M16.5 3.8h3.3v3.3"/>
        </g>
      </svg>
      <div class="service-label">Reporting and<br>Forecasting</div>
    </div>
  </div>

  <div class="footer-label">08 | OUTPOST LATTICE ADVISORS</div>
  <div class="footer-rule"></div>
</div>
</body>
</html>
```